Flyer Design Project

I need a flyer design to pass out to promote my business and to bring in more business. My business is a auto body shop and we do auto body repair on all makes and models. We take all types of insurance work and cash deals are welcome. We type of paint we use is KTV so i would like the KTV logo somewhere on the flyer.I would also like to include that we offer free estimates.
Updates

I forgot to include the following information to my shop

Address : 3847 N. Willowmere Ave
                 San Mateo, Ca 94402

Tel : 650-318-4962

Website : www.DelvaCollision.com

please include that cash deals are welcome, we offer 24 hours drop off service, and we offer mobile estimate service

Industry/Entity Type

Insurance

Requirements
Must have
• Must have my company logo in it. Must be eye catching.

```html
<!DOCTYPE html>
<html lang="en">
<head>
<meta charset="utf-8">
<title>Delva Collision – Auto Body Flyer</title>
<link rel="stylesheet" href="https://fonts.googleapis.com/css2?family=Oswald:wght@500;600;700&display=swap">
<style>
  :root {
    --ink: #050505;
    --brand-red: #a30f0f;
    --deep-red: #8c0a0a;
    --paper: #ffffff;
    --text-light: #ffffff;
    --shop-beige: #c9b8a2;
    --car-red: #e0221e;
  }
  * { margin: 0; padding: 0; box-sizing: border-box; }
  html, body { width: 927px; height: 1200px; overflow: hidden; background: var(--ink); }
  .flyer {
    position: relative;
    width: 927px;
    height: 1200px;
    background: var(--ink);
    font-family: "Oswald", "Arial Narrow", sans-serif;
    color: var(--text-light);
    overflow: hidden;
  }
  .corner-flag { position: absolute; left: 0; top: 0; width: 186px; height: 186px; }
  .corner-flag__text {
    position: absolute;
    left: 4px; top: 40px;
    width: 140px;
    transform: rotate(-45deg);
    font-weight: 600;
    font-size: 19px;
    line-height: 1.05;
    text-align: center;
  }
  .logo-box {
    position: absolute;
    left: 310px; top: 0;
    width: 326px; height: 161px;
    background: var(--paper);
    display: flex; align-items: center; justify-content: center; gap: 12px;
  }
  .logo-box__dot { width: 22px; height: 22px; border-radius: 50%; background: var(--brand-red); }
  .logo-box__name {
    font-weight: 700;
    font-size: 40px;
    color: var(--brand-red);
    letter-spacing: 0.5px;
  }
  .web-address {
    position: absolute;
    left: 310px; width: 326px; top: 168px;
    text-align: center;
    font-weight: 600;
    font-size: 24px;
  }
  .info-panel {
    position: absolute;
    left: 55px; top: 231px;
    width: 817px; height: 274px;
    background: var(--brand-red);
    text-align: center;
    padding-top: 19px;
  }
  .info-panel__line { font-weight: 600; font-size: 25px; line-height: 32.5px; }
  .info-panel__tagline { font-weight: 600; font-size: 34px; line-height: 44px; margin-top: 4px; }
  .before-frame {
    position: absolute;
    left: 23px; top: 522px;
    width: 306px; height: 361px;
    background: var(--paper);
    padding: 8px;
  }
  .before-frame__photo {
    position: relative;
    width: 100%; height: 100%;
    background: linear-gradient(180deg, #d8c9b6 0%, var(--shop-beige) 40%, #b43a2c 62%, #9c6c48 100%);
  }
  .photo-label {
    position: absolute;
    font-weight: 600;
    font-size: 25px;
    text-shadow: 0 0 3px #000;
  }
  .before-frame .photo-label { left: 108px; bottom: 2px; }
  .after-photo {
    position: absolute;
    left: 343px; top: 524px;
    width: 561px; height: 352px;
    background: radial-gradient(ellipse 48% 34% at 53% 52%, var(--car-red) 0%, #b51512 55%, #120404 85%, var(--ink) 100%);
  }
  .after-label { position: absolute; left: 588px; top: 852px; font-weight: 600; font-size: 25px; }
  .services-panel {
    position: absolute;
    left: 55px; top: 901px;
    width: 817px; height: 244px;
    background: var(--brand-red);
    text-align: center;
    padding-top: 20px;
  }
  .services-panel__title { font-weight: 600; font-size: 27px; line-height: 32px; margin-bottom: 2px; }
  .services-panel__list { list-style: none; }
  .services-panel__list li { font-weight: 500; font-size: 19px; line-height: 25px; }
  .paint-badge {
    position: absolute;
    left: 763px; top: 1074px;
    width: 109px; height: 71px;
    background: var(--paper);
    display: flex; align-items: center; justify-content: center; gap: 8px;
  }
  .paint-badge__mark { width: 14px; height: 14px; background: var(--brand-red); }
  .paint-badge__name { font-weight: 700; font-size: 28px; color: var(--brand-red); }
</style>
</head>
<body>
<main class="flyer">
  <svg class="corner-flag" viewBox="0 0 186 186" aria-hidden="true">
    <polygon points="0,0 186,0 0,186" fill="var(--deep-red)"/>
  </svg>
  <div class="corner-flag__text">We offer<br>free estimates</div>

  <header class="logo-box">
    <span class="logo-box__dot"></span>
    <span class="logo-box__name">Delva Collision</span>
  </header>
  <div class="web-address">www.DelvaCollision.com</div>

  <section class="info-panel">
    <p class="info-panel__line">We do auto body repair on all makes and models!</p>
    <p class="info-panel__line">We take all types of insurance work and cash deals are welcome!</p>
    <p class="info-panel__line">Address : 3847 N. Willowmere Ave</p>
    <p class="info-panel__line">San Mateo, Ca 94402</p>
    <p class="info-panel__line">Tel : 650-318-4962</p>
    <p class="info-panel__tagline">Delva Collision Proudly Serving Entire Bay Area</p>
  </section>

  <figure class="before-frame">
    <div class="before-frame__photo" role="img" aria-label="Technician sanding a red sports car body inside the repair shop before refinishing">
      <span class="photo-label">BEFORE</span>
    </div>
  </figure>

  <div class="after-photo" role="img" aria-label="Fully refinished glossy red sports car on a black background"></div>
  <span class="after-label">AFTER</span>

  <section class="services-panel">
    <h2 class="services-panel__title">SERVICES</h2>
    <ul class="services-panel__list">
      <li>• Collision Repairs &nbsp;• Major and minor accident damage repair</li>
      <li>• All Foreign and Domestic makes and models • Exact frame straightening on premises</li>
      <li>• Expert paint matching and refinishing • Paintless dent repair</li>
      <li>• Free damage repair estimates • Bumper spot refinishing</li>
      <li>• Windshield Replacement &nbsp;• Expert Unibody Reconstruction</li>
      <li>• Dent Removal • Car Detailing</li>
      <li>• 24 Hour Drop Off Service • Mobile Estimate Service</li>
    </ul>
  </section>
  <div class="paint-badge">
    <span class="paint-badge__mark"></span>
    <span class="paint-badge__name">KTV</span>
  </div>
</main>
</body>
</html>
```